Brasko Construction Business Card

I need a business card design for my company.
We are a construction/machinery company.
I would like to see my logo on the front of the card and my details on the other side
I would like the card to be black or dark grey in colour,with my logo as i send it or modified with a lighter blue colour
I would like to see the design kept fairly simple,but eye catching at the same time
Industry/Entity Type
Business
Contact Information for Business Card
Name
Phone Number
Address
Email
Colors
00a990
1b1b1b
000000
474747
ececec

```html
<!DOCTYPE html>
<html lang="en">
<head>
<meta charset="utf-8">
<title>Brasko Construction Business Card</title>
<link rel="stylesheet" href="https://fonts.googleapis.com/css2?family=Open+Sans:wght@400;600;700;800&display=swap">
<style>
  :root {
    --teal: #00a990;
    --teal-light: #2fc4ad;
    --ink: #1b1b1b;
    --black: #000000;
    --grey: #474747;
    --paper: #ececec;
    --stage: #dcdcdc;
  }
  html, body {
    margin: 0;
    width: 1200px;
    height: 913px;
    overflow: hidden;
    background: var(--stage);
    font-family: "Open Sans", sans-serif;
  }
  .canvas {
    position: relative;
    width: 1200px;
    height: 913px;
  }
  .card {
    position: absolute;
    width: 520px;
    height: 300px;
    border-radius: 16px;
    box-shadow: 0 10px 24px rgba(0,0,0,.28);
  }
  .card--front { left: 80px; top: 130px; }
  .card--back { left: 600px; top: 480px; }
  .card svg { display: block; width: 520px; height: 300px; }
  .brand-name { font-family: "Open Sans", sans-serif; font-weight: 800; fill: var(--paper); letter-spacing: 3px; }
  .brand-name--back { fill: var(--ink); }
  .person-name { font-weight: 700; font-size: 22px; fill: #ffffff; }
  .person-role { font-weight: 400; font-size: 14px; fill: var(--teal); }
  .contact-line { font-weight: 400; font-size: 14px; fill: #ffffff; }
</style>
</head>
<body>
<main class="canvas">

  <section class="card card--front" aria-label="Card front with contact details">
    <svg viewBox="0 0 520 300" xmlns="http://www.w3.org/2000/svg">
      <defs>
        <clipPath id="front-shape"><rect width="520" height="300" rx="16"/></clipPath>
        <linearGradient id="front-upper" x1="0" y1="0" x2="1" y2="1">
          <stop offset="0" stop-color="#2a2a2a"/>
          <stop offset="1" stop-color="#5a5a5a"/>
        </linearGradient>
        <linearGradient id="front-lower" x1="0" y1="0" x2="1" y2="1">
          <stop offset="0" stop-color="#1b1b1b"/>
          <stop offset="1" stop-color="#3a3a3a"/>
        </linearGradient>
      </defs>
      <g clip-path="url(#front-shape)">
        <rect class="front-base" width="520" height="300" fill="url(#front-lower)"/>
        <path class="front-upper-panel" d="M0,0 H490 Q380,200 0,205 Z" fill="url(#front-upper)"/>
        <path class="front-curve" d="M490,0 Q380,200 0,205" fill="none" stroke="#ffffff" stroke-width="4"/>
        <line class="front-divider" x1="345" y1="140" x2="500" y2="140" stroke="#6a6a6a" stroke-width="1"/>
        <line class="front-divider" x1="178" y1="238" x2="500" y2="238" stroke="#6a6a6a" stroke-width="1"/>
        <circle class="name-marker" cx="0" cy="254" r="20" fill="var(--teal)"/>
      </g>

      <text class="brand-name" x="190" y="82" font-size="38" text-anchor="middle">BRASKO</text>
      <text class="brand-name" x="190" y="106" font-size="15" text-anchor="middle" letter-spacing="5">CONSTRUCTION</text>

      <text class="contact-line" x="478" y="168" text-anchor="end">+33 2460-5132</text>
      <text class="contact-line" x="478" y="192" text-anchor="end">info@braskobuild.com</text>
      <text class="contact-line" x="478" y="216" text-anchor="end">18 Harbor Street Westport VIC 3300</text>

      <g class="icon icon--phone" transform="translate(484,157)" fill="var(--teal)">
        <path d="M2,0 h3 l1,3 -2,1.5 a8,8 0 0 0 3.5,3.5 l1.5,-2 3,1 v3 a1,1 0 0 1 -1,1 A11,11 0 0 1 1,1 a1,1 0 0 1 1,-1z"/>
      </g>
      <g class="icon icon--mail" transform="translate(484,183)">
        <rect x="0" y="0" width="13" height="9" rx="1" fill="none" stroke="var(--teal)" stroke-width="1.5"/>
        <path d="M0,0 L6.5,5 L13,0" fill="none" stroke="var(--teal)" stroke-width="1.5"/>
      </g>
      <g class="icon icon--pin" transform="translate(486,203)" fill="var(--teal)">
        <path d="M5,0 a5,5 0 0 1 5,5 c0,4 -5,9 -5,9 s-5,-5 -5,-9 a5,5 0 0 1 5,-5z"/>
        <circle cx="5" cy="5" r="2" fill="#1b1b1b"/>
      </g>

      <text class="person-name" x="32" y="246">Lena Marsh</text>
      <text class="person-role" x="32" y="268">Director</text>
    </svg>
  </section>

  <section class="card card--back" aria-label="Card back with company name">
    <svg viewBox="0 0 520 300" xmlns="http://www.w3.org/2000/svg">
      <defs>
        <clipPath id="back-shape"><rect width="520" height="300" rx="16"/></clipPath>
        <linearGradient id="back-teal" x1="0" y1="0" x2="1" y2="1">
          <stop offset="0" stop-color="var(--teal-light)"/>
          <stop offset="1" stop-color="var(--teal)"/>
        </linearGradient>
      </defs>
      <g clip-path="url(#back-shape)">
        <rect class="back-base" width="520" height="300" fill="var(--ink)"/>
        <path class="back-teal-panel" d="M520,55 Q250,80 40,300 H520 Z" fill="url(#back-teal)"/>
        <path class="back-curve" d="M520,55 Q250,80 40,300" fill="none" stroke="#ffffff" stroke-width="4"/>
      </g>
      <text class="brand-name brand-name--back" x="320" y="205" font-size="54" text-anchor="middle">BRASKO</text>
    </svg>
  </section>

</main>
</body>
</html>
```